Corporate Design für neue Personaldienstleistung Firma - Ruf Mich -
Zielgruppe
Wir sind noch in der Gründungsphase unseres Personaldienstleistungsunternemens.
Ruf Mich Personaldienstleistungen GmbH & Co. KG
Brunnwiesenweg 8
D-67412 Rebenau an der Weinstraße
Wir sind zwei Partner und sehen UNS als Kompetenter Ansprechpartner wenn es um Personalbedarf geht.
Wir spezialisieren uns aber ganz klar auf
- Automobil
- Motorsport
- Industrie
Wir speziallisieren uns auf diesen Sektur mit Ingenieuren, Technikern und Fachkräften und keinen helfern.
Zielgruppe sind
- Motorsport höchstes leavel
- Die deutschen Automobilbauer
- und die Großen der Industrie
- Kein Handwerk
Wir vermitteln Spezialisten und Führungskräfte für den Bereichen Automobil Motorsport und Industrie
- In Festanstellungen
- In freiberufliche Projekte
- Personalgestellung (Arbeitnehmer Überlassung)
- Projektgeschäft.
Wir Gründer können zahlreiche Erfolge in der Vermittlung sowohl bei kleinen, Mittelständigen als auch bei den Größen der deutschen Industrie vorweisen.
Wir kombinieren unsere eigene gewonnene Berufserfahrung und kombinieren diese Expertise mit unserer großen Flexibilität unseres kompakten Unternehmens.
Unser Ziel:
Wir denken über kurzfristigen Profit hinaus und engagieren uns nachhaltig - für unsere Kunden und Kandidaten
Unser Handeln ist auf eine langfristige Partnerschaft ausgerichtet
Wir verstehen uns als Ihr Problemlöser
Persönlicher Einsatz
Technischer Sachverstand
Schnelligkeit im Rekrutierung-Prozess
Aufgabenstellung
Wir sind offen für das Logo das soll aber schnörkellos sein wobei es für alle Medien dann nutzbar sein soll
Wir hätten gerne
- Briefpapier
- Visitenkarten
- layout für Notizblock A4 / A5

```html
<!DOCTYPE html>
<html lang="de">
<head>
<meta charset="utf-8">
<title>Ruf Mich – Corporate Design</title>
<link href="https://fonts.googleapis.com/css2?family=Montserrat:wght@400;500;600;700&display=swap" rel="stylesheet">
<style>
  :root{
    --orange:#f07e22;
    --ink:#2b2f2b;
    --stone:#dedad6;
    --slate:#a6a6a6;
    --paper:#ffffff;
    --window:#d0d0d0;
    --rule:#9a9a9a;
    --grid:#cfcfcf;
  }
  *{margin:0;padding:0;box-sizing:border-box}
  html,body{width:1200px;height:1200px;overflow:hidden;font-family:"Montserrat",sans-serif;color:var(--ink)}
  .canvas{position:relative;width:1200px;height:1200px;background:var(--paper)}
  .zone-stationery{position:absolute;left:0;top:0;width:1200px;height:659px;background:var(--stone)}
  .zone-cards{position:absolute;left:0;top:659px;width:1200px;height:328px;background:var(--slate)}
  .footer-strip{position:absolute;left:0;top:1190px;width:1200px;height:10px;background:var(--ink)}

  .wordmark{font-family:"Montserrat",sans-serif;font-weight:500;letter-spacing:.01em;white-space:nowrap;line-height:1}
  .wordmark-dot{display:inline-block;border-radius:50%;background:var(--orange);vertical-align:middle}

  /* Notepad */
  .notepad{position:absolute;left:71px;top:67px;width:381px;height:537px;background:var(--paper);border:1px solid var(--ink);overflow:hidden}
  .notepad .wordmark{position:absolute;left:20px;top:24px;font-size:19px;color:var(--ink)}
  .notepad .wordmark-dot{width:7px;height:7px;margin-left:4px}
  .field{position:absolute;font-size:6px;line-height:7px;font-weight:500;letter-spacing:.03em}
  .field-rule{position:absolute;left:22px;width:338px;height:1px;background:var(--rule)}
  .notepad-grid{position:absolute;left:0;top:104px;right:0;bottom:0;
    background-image:linear-gradient(var(--grid) 1px,transparent 1px),linear-gradient(90deg,var(--grid) 1px,transparent 1px);
    background-size:12.8px 12.8px}

  /* Envelope */
  .envelope{position:absolute;left:499px;top:146px;width:625px;height:319px;background:var(--paper)}
  .envelope .wordmark{position:absolute;left:30px;top:86px;font-size:25px;color:var(--ink)}
  .envelope .wordmark-dot{width:9px;height:9px;margin-left:5px}
  .address-window{position:absolute;left:53px;top:142px;width:283px;height:126px;border-radius:13px;background:var(--window)}
  .envelope-band{position:absolute;left:0;top:292px;width:441px;height:27px;background:var(--orange)}
  .envelope-url{position:absolute;left:441px;top:292px;width:184px;height:27px;background:var(--ink);color:var(--paper);font-size:10px;font-weight:700;padding:4px 0 0 23px;letter-spacing:.02em}

  /* Pen */
  .pen{position:absolute;left:0;top:0;width:1200px;height:1200px;pointer-events:none}

  /* Business cards */
  .card{position:absolute;top:706px;width:386px;height:229px}
  .card-front{left:176px;background:var(--ink);color:var(--paper)}
  .card-front .wordmark{position:absolute;left:54px;top:92px;font-size:36px;color:var(--paper)}
  .card-front .wordmark-dot{width:12px;height:12px;margin-left:8px}
  .card-address{position:absolute;left:0;right:0;top:152px;text-align:center;font-size:11.3px;line-height:16.6px;letter-spacing:.03em}
  .card-address strong{font-weight:700}
  .card-address .sep{display:inline-block;width:4px;height:4px;border-radius:50%;background:var(--orange);vertical-align:middle;margin:0 14px 0 10px}
  .card-url{position:absolute;left:0;right:0;top:193px;text-align:center;color:var(--orange);font-weight:700;font-size:11.5px;letter-spacing:.04em}

  .card-back{left:622px;background:var(--paper)}
  .person-name{position:absolute;left:197px;top:83px;font-size:11.5px;font-weight:700;letter-spacing:.08em}
  .person-role{position:absolute;left:197px;top:101px;font-size:10.5px;letter-spacing:.04em}
  .contact-list{position:absolute;left:194px;top:134px;list-style:none;font-size:10.8px;letter-spacing:.03em}
  .contact-list li{display:flex;align-items:center;height:18.3px}
  .contact-list svg{width:11px;height:11px;margin-right:4px;flex:none}

  /* Logo lockup */
  .lockup{position:absolute;left:0;top:1040px;width:1200px;text-align:center}
  .lockup .wordmark{font-size:66px;color:var(--ink)}
  .lockup .wordmark-dot{width:22px;height:22px;margin-left:14px;vertical-align:baseline}
</style>
</head>
<body>
<div class="canvas">
  <section class="zone-stationery">
    <article class="notepad">
      <div class="wordmark">RufMich<span class="wordmark-dot"></span></div>
      <span class="field" style="left:22px;top:59px">KUNDE</span>
      <span class="field" style="left:148px;top:59px">PROJEKT</span>
      <span class="field" style="left:275px;top:59px">DATUM</span>
      <div class="field-rule" style="top:68px"></div>
      <span class="field" style="left:22px;top:82px">BEARBEITER</span>
      <span class="field" style="left:148px;top:82px">BESPRECHUNGSANLASS</span>
      <div class="field-rule" style="top:92px"></div>
      <div class="notepad-grid"></div>
    </article>

    <article class="envelope">
      <div class="wordmark">RufMich<span class="wordmark-dot"></span></div>
      <div class="address-window"></div>
      <div class="envelope-band"></div>
      <div class="envelope-url">www.rufmich-personal.de</div>
    </article>
  </section>

  <section class="zone-cards">
  </section>

  <svg class="pen" viewBox="0 0 1872 1872" aria-hidden="true">
    <g fill="#fff" stroke="#2b2f2b" stroke-width="2">
      <rect x="1697" y="862" width="68" height="37"/>
      <path d="M800 880 L828 873 L828 867 C920 856 990 849 1050 848 L1625 848 L1695 852 C1700 860 1700 905 1695 912 L1625 916 L1050 914 C990 913 920 905 828 893 L828 888 L800 885 Z"/>
      <path d="M1625 848 L1625 916"/>
      <path d="M828 873 L828 888"/>
      <path d="M1385 820 C1380 825 1382 832 1390 834 L1625 845 C1640 850 1655 855 1663 862 L1668 858 C1650 840 1620 825 1560 820 Z"/>
    </g>
    <text x="1388" y="893" font-family="Montserrat, sans-serif" font-weight="500" font-size="40" fill="#2b2f2b">RufMich</text>
    <circle cx="1578" cy="881" r="5" fill="#f07e22"/>
  </svg>

  <article class="card card-front">
    <div class="wordmark">RufMich<span class="wordmark-dot"></span></div>
    <p class="card-address"><strong>Ruf Mich</strong> Personaldienstleistungen GmbH &amp; Co. KG<br>Brunnwiesenweg 8<span class="sep"></span>D-67412 Rebenau an der Weinstraße</p>
    <p class="card-url">www.rufmich-personal.de</p>
  </article>

  <article class="card card-back">
    <p class="person-name">JONAS BEISPIEL</p>
    <p class="person-role">Geschäftsführer</p>
    <ul class="contact-list">
      <li><svg viewBox="0 0 12 12"><circle cx="6" cy="6" r="5" fill="none" stroke="#2b2f2b" stroke-width="1.2"/><circle cx="6" cy="6" r="2" fill="none" stroke="#2b2f2b" stroke-width="1.2"/></svg>info@rufmich-personal.de</li>
      <li><svg viewBox="0 0 12 12"><circle cx="6" cy="6" r="5.3" fill="none" stroke="#2b2f2b" stroke-width="1"/><path d="M4 3.2 L5 4.6 L4.4 5.3 C4.9 6.3 5.7 7.1 6.7 7.6 L7.4 7 L8.8 8 L8.2 9 C6 8.8 3.2 6 3 3.8 Z" fill="#2b2f2b"/></svg>+49 0456 / 78123</li>
      <li><svg viewBox="0 0 12 12"><rect x="1" y="4" width="10" height="7" rx="1" fill="none" stroke="#2b2f2b" stroke-width="1"/><rect x="3" y="1" width="6" height="3" fill="none" stroke="#2b2f2b" stroke-width="1"/></svg>+49 0222 / 34 567 89</li>
      <li><svg viewBox="0 0 12 12"><rect x="3" y="1" width="6" height="10" rx="1" fill="none" stroke="#2b2f2b" stroke-width="1.1"/></svg>+49 0456 / 789012</li>
    </ul>
  </article>

  <div class="lockup">
    <div class="wordmark">RufMich<span class="wordmark-dot"></span></div>
  </div>

  <div class="footer-strip"></div>
</div>
</body>
</html>
```